Testing form re-design

I have 2 new testing forms in a very basic format, I need them updated to look similar to our other testing forms. Attached are the two new forms (Dermatology and GI) as well as a couple of our Original normal testing forms to compare them to. Needs to be in an editable PSD file incase I need to change the verbiage in the future. Also a few addendums to the Dermatology form - Need to add a form field for "Clinical Impression" as well as "Clinical History" with spaces 2 inches to handwrite next to them.

Industry/Entity Type

Healthcare

Font styles to use
Sans Serif

Colors

Designer to choose colors to be used in the design.

Requirements
Must have
• All the information on the current forms

```html
<!DOCTYPE html>
<html lang="en">
<head>
<meta charset="utf-8">
<title>Dermatology Test Requisition Form</title>
<link rel="stylesheet" href="https://fonts.googleapis.com/css2?family=Poppins:wght@500;600;700;800&family=Roboto:wght@400;500;700&display=swap">
<style>
:root{
  --band:#cfd9ec;
  --ink:#141414;
  --red:#d0021b;
  --brand:#1e7cc4;
  --rule:#222;
  --panel-gray:#dcdcdc;
  --badge:#b9c6de;
  --paper:#fff;
}
*{margin:0;padding:0;box-sizing:border-box}
html,body{width:729px;height:1200px;overflow:hidden;background:var(--paper)}
.canvas{width:729px;height:1200px;overflow:hidden;position:relative}
.sheet{position:absolute;left:0;top:0;width:1495px;height:2461px;transform:scale(0.48763);transform-origin:0 0;font-family:Roboto,Arial,sans-serif;color:var(--ink)}
.t{position:absolute;white-space:nowrap;line-height:1}
.hl{position:absolute;height:2px;background:var(--rule)}
.vl{position:absolute;width:2px;background:var(--rule)}
.thick{height:3px}
.cb{display:inline-block;width:15px;height:15px;border:1.6px solid var(--ink);margin-right:3px;vertical-align:-1px}
.cb.lg{width:17px;height:17px}
.req{color:var(--red)}
/* header */
.header{position:absolute;left:22px;top:18px;width:1452px;height:203px;background:var(--band)}
.brand-dot{position:absolute;left:108px;top:48px;width:80px;height:80px;border-radius:50%;background:var(--brand)}
.brand-name{position:absolute;left:40px;top:134px;width:256px;text-align:center;font-family:Poppins,sans-serif;font-weight:700;font-size:30px;color:var(--brand);line-height:1.05}
.title{position:absolute;left:300px;width:900px;text-align:center;font-family:Poppins,sans-serif;line-height:1;white-space:nowrap}
.title.main{top:48px;font-size:44px;font-weight:800;letter-spacing:.3px}
.title.addr{top:97px;font-size:31px;font-weight:500}
.title.contact{top:160px;font-size:31px;font-weight:500}
.badge{position:absolute;left:1218px;top:66px;width:226px;height:100px;border-radius:10px;background:var(--badge)}
/* frame */
.frame{position:absolute;left:22px;top:222px;width:1453px;height:1784px;border:2px solid var(--rule)}
.sec-head{position:absolute;text-align:center;font-weight:500;font-size:26px;line-height:1;white-space:nowrap}
.lbl{font-size:16px}
.sm{font-size:15px}
.opt{font-size:19px}
.bignum{font-size:40px;font-weight:700}
.amr-title{font-size:44px;font-weight:500;text-decoration:underline;text-decoration-thickness:3px;text-underline-offset:6px}
.amr-item{font-size:19px;font-weight:500}
.org{font-size:24px;font-weight:500}
.group-head{font-size:26px;font-weight:700}
.pcr-band{position:absolute;left:699px;top:1035px;width:775px;height:42px;background:var(--panel-gray)}
.pcr-box{position:absolute;left:837px;top:1046px;width:44px;height:20px;border:3px solid var(--ink)}
.pcr-title{font-size:34px;font-weight:700;text-decoration:underline;text-decoration-thickness:2px;text-underline-offset:5px}
.clin-label{font-size:22px;font-weight:700}
.write-line{position:absolute;height:1.5px;background:var(--rule)}
.fine{position:absolute;left:22px;width:1455px;font-size:13.4px;line-height:17.6px}
.sig-line{position:absolute;height:2px;background:var(--rule)}
</style>
</head>
<body>
<div class="canvas">
<div class="sheet">

  <header class="header">
    <div class="brand-dot"></div>
    <div class="brand-name">CRESTLINE LABS</div>
    <div class="title main">DERMATOLOGY TEST REQUISITION FORM</div>
    <div class="title addr">4120 Harborview Pkwy Suite 210, Lakeview, MI 48900</div>
    <div class="title contact">(555) 301-0147 | www.crestlinelabs.example</div>
    <div class="badge"></div>
  </header>

  <div class="frame"></div>
  <div class="vl" style="left:696px;top:222px;height:1450px"></div>

  <!-- Ordering physician -->
  <div class="sec-head" style="left:22px;width:675px;top:226px">Ordering Physician/Laboratory</div>
  <div class="hl" style="left:22px;top:255px;width:1453px"></div>
  <div class="t lbl req" style="left:30px;top:261px;line-height:1.3">(Required: Include the ordering physician’s first &amp; last name, NPI, practice name,<br>complete address, phone number and fax number.)</div>
  <div class="hl" style="left:22px;top:638px;width:675px"></div>
  <div class="t lbl" style="left:29px;top:643px">Physician to recieve additional result report:</div>
  <div class="hl" style="left:22px;top:677px;width:675px"></div>
  <div class="t lbl" style="left:29px;top:681px">Physician’s Signature:</div>
  <div class="vl" style="left:473px;top:677px;height:56px"></div>
  <div class="t lbl" style="left:480px;top:681px">Date:</div>
  <div class="hl thick" style="left:22px;top:732px;width:675px"></div>

  <!-- Biopsy -->
  <div class="sec-head" style="left:22px;width:675px;top:741px">Biopsy Information</div>
  <div class="hl thick" style="left:22px;top:772px;width:675px"></div>
  <div class="t" style="left:29px;top:778px;font-size:19px;font-weight:500">ICD10 codes <span class="req">(required)</span>:</div>
  <div class="hl" style="left:22px;top:818px;width:675px"></div>
  <div class="t lbl req" style="left:27px;top:824px">(Date Collected Req):</div>
  <div class="vl" style="left:205px;top:818px;height:52px"></div>
  <div class="t lbl" style="left:211px;top:824px">Time Collected:</div>
  <div class="vl" style="left:351px;top:818px;height:52px"></div>
  <div class="t lbl" style="left:356px;top:824px">Collector Signature:</div>
  <div class="vl" style="left:526px;top:818px;height:52px"></div>
  <div class="t lbl" style="left:532px;top:824px">No. vials collected:</div>
  <div class="hl" style="left:22px;top:870px;width:675px"></div>

  <div class="t lbl" style="left:30px;top:878px">Type:</div>
  <div class="t opt" style="left:80px;top:878px"><i class="cb lg"></i>Punch Biopsy</div>
  <div class="t opt" style="left:80px;top:900px"><i class="cb lg"></i>Punch Excision (Ink)</div>
  <div class="t opt" style="left:80px;top:922px"><i class="cb lg"></i>Shave Biopsy</div>
  <div class="t opt" style="left:291px;top:878px"><i class="cb lg"></i>Shave Removal (Ink)</div>
  <div class="t opt" style="left:291px;top:900px"><i class="cb lg"></i>Excision (Ink)</div>
  <div class="t opt" style="left:291px;top:922px"><i class="cb lg"></i>Currettage</div>
  <div class="t opt" style="left:503px;top:878px"><i class="cb lg"></i>Alopecia Sections</div>
  <div class="t opt" style="left:503px;top:900px"><i class="cb lg"></i>D|F</div>
  <div class="hl" style="left:22px;top:948px;width:675px"></div>

  <!-- Site 1 -->
  <div class="t bignum" style="left:30px;top:953px">1</div>
  <div class="t lbl" style="left:55px;top:969px">Site:</div>
  <div class="hl" style="left:96px;top:982px;width:601px;height:1.5px"></div>
  <div class="hl" style="left:22px;top:984px;width:675px"></div>
  <div class="t" style="left:30px;top:992px;font-size:19px;font-weight:700">Clinical Findings</div>
  <div class="t opt" style="left:80px;top:1014px"><i class="cb lg"></i>Nevus Atypical</div>
  <div class="t opt" style="left:80px;top:1036px"><i class="cb lg"></i>Melanoma</div>
  <div class="t opt" style="left:80px;top:1058px"><i class="cb lg"></i>BCC</div>
  <div class="t opt" style="left:291px;top:1014px"><i class="cb lg"></i>SCC</div>
  <div class="t opt" style="left:291px;top:1036px"><i class="cb lg"></i>AK</div>
  <div class="t opt" style="left:291px;top:1058px"><i class="cb lg"></i>SK</div>
  <div class="t opt" style="left:503px;top:1014px"><i class="cb lg"></i>FEP</div>
  <div class="t opt" style="left:503px;top:1036px"><i class="cb lg"></i>DF</div>
  <div class="t opt" style="left:503px;top:1058px"><i class="cb lg"></i>VV</div>
  <div class="hl" style="left:22px;top:1082px;width:675px"></div>

  <!-- Site 2 -->
  <div class="t bignum" style="left:30px;top:1086px">2</div>
  <div class="t lbl" style="left:55px;top:1102px">Site:</div>
  <div class="hl" style="left:96px;top:1114px;width:601px;height:1.5px"></div>
  <div class="hl" style="left:22px;top:1116px;width:675px"></div>
  <div class="t" style="left:30px;top:1122px;font-size:19px;font-weight:700">Clinical Findings</div>
  <div class="t opt" style="left:80px;top:1146px"><i class="cb lg"></i>Nevus Atypical</div>
  <div class="t opt" style="left:80px;top:1168px"><i class="cb lg"></i>Melanoma</div>
  <div class="t opt" style="left:80px;top:1190px"><i class="cb lg"></i>BCC</div>
  <div class="t opt" style="left:291px;top:1146px"><i class="cb lg"></i>SCC</div>
  <div class="t opt" style="left:291px;top:1168px"><i class="cb lg"></i>AK</div>
  <div class="t opt" style="left:291px;top:1190px"><i class="cb lg"></i>SK</div>
  <div class="t opt" style="left:503px;top:1146px"><i class="cb lg"></i>FEP</div>
  <div class="t opt" style="left:503px;top:1168px"><i class="cb lg"></i>DF</div>
  <div class="t opt" style="left:503px;top:1190px"><i class="cb lg"></i>VV</div>
  <div class="hl" style="left:22px;top:1215px;width:675px"></div>

  <!-- Site 3 -->
  <div class="t bignum" style="left:30px;top:1219px">3</div>
  <div class="t lbl" style="left:55px;top:1236px">Site:</div>
  <div class="hl" style="left:96px;top:1248px;width:601px;height:1.5px"></div>
  <div class="hl" style="left:22px;top:1250px;width:675px"></div>
  <div class="t" style="left:30px;top:1256px;font-size:19px;font-weight:700">Clinical Findings</div>
  <div class="t opt" style="left:80px;top:1279px"><i class="cb lg"></i>Nevus Atypical</div>
  <div class="t opt" style="left:80px;top:1301px"><i class="cb lg"></i>Melanoma</div>
  <div class="t opt" style="left:80px;top:1323px"><i class="cb lg"></i>BCC</div>
  <div class="t opt" style="left:291px;top:1279px"><i class="cb lg"></i>SCC</div>
  <div class="t opt" style="left:291px;top:1301px"><i class="cb lg"></i>AK</div>
  <div class="t opt" style="left:291px;top:1323px"><i class="cb lg"></i>SK</div>
  <div class="t opt" style="left:503px;top:1279px"><i class="cb lg"></i>FEP</div>
  <div class="t opt" style="left:503px;top:1301px"><i class="cb lg"></i>DF</div>
  <div class="t opt" style="left:503px;top:1323px"><i class="cb lg"></i>VV</div>
  <div class="hl" style="left:22px;top:1346px;width:675px"></div>

  <div class="t" style="left:29px;top:1353px;font-size:22px">1499 <i class="cb lg"></i>Biopsy (H&amp;E Stain)</div>
  <div class="t" style="left:29px;top:1384px;font-size:22px">1499 <i class="cb lg"></i>Nail with Nail Bed Biopsy with PAS</div>
  <div class="hl thick" style="left:22px;top:1411px;width:675px"></div>

  <!-- AMR panel -->
  <div class="t amr-title" style="left:48px;top:1427px">Antimicrobial Resistance Panel</div>
  <div class="t amr-item" style="left:41px;top:1492px;line-height:27.6px">KPC — Carbapenem resistance<br>NDM — Carbapenem resistance<br>VIM — Carbapenem resistance<br>IMP — Carbapenem resistance<br>qnr — Quinolone resistance<br>vanB — Vancomycin resistance</div>
  <div class="t amr-item" style="left:361px;top:1492px;line-height:27.6px">OXA-48 — Carbapenem resistance<br>mecA/mecC — Methicillin resistance<br>CTX-M ESBL<br>sul — Sulfonamide resistance<br>vanA — Vancomycin resistance<br>dfrA — Trimethoprim resistance</div>

  <!-- Patient information -->
  <div class="sec-head" style="left:697px;width:777px;top:226px">Patient Information (Please Print)</div>
  <div class="t lbl req" style="left:711px;top:261px">Name (Last, First) (Required):</div>
  <div class="hl" style="left:697px;top:294px;width:777px"></div>
  <div class="t lbl" style="left:711px;top:301px">In Care of:</div>
  <div class="hl" style="left:697px;top:334px;width:777px"></div>
  <div class="t lbl" style="left:711px;top:341px">Patient Address:</div>
  <div class="hl" style="left:697px;top:377px;width:777px"></div>
  <div class="t lbl" style="left:711px;top:383px">City:</div>
  <div class="vl" style="left:1010px;top:377px;height:43px"></div>
  <div class="t lbl" style="left:1018px;top:383px">State:</div>
  <div class="vl" style="left:1142px;top:377px;height:43px"></div>
  <div class="t lbl" style="left:1150px;top:383px">Zip:</div>
  <div class="hl" style="left:697px;top:420px;width:777px"></div>
  <div class="t lbl req" style="left:711px;top:425px">Assigned Sex at Birth (Required):</div>
  <div class="t lbl" style="left:748px;top:446px"><i class="cb"></i>Female</div>
  <div class="t lbl" style="left:881px;top:446px"><i class="cb"></i>Male</div>
  <div class="vl" style="left:985px;top:420px;height:43px"></div>
  <div class="t lbl req" style="left:991px;top:425px">Date of Birth (Required):</div>
  <div class="vl" style="left:1262px;top:420px;height:43px"></div>
  <div class="t lbl" style="left:1270px;top:423px">Patient ID#:</div>
  <div class="hl" style="left:697px;top:463px;width:777px"></div>
  <div class="t lbl req" style="left:711px;top:470px">Phone Number:</div>
  <div class="t lbl" style="left:1282px;top:469px"><i class="cb"></i>Cell Phone</div>
  <div class="t lbl" style="left:1282px;top:487px"><i class="cb"></i>Home Phone</div>
  <div class="hl" style="left:697px;top:507px;width:777px"></div>

  <div class="t sm" style="left:711px;top:514px"><b>Race:</b> <i class="cb"></i>Alaska Native or American Indian &nbsp;<i class="cb"></i>Black or African American</div>
  <div class="t sm" style="left:711px;top:535px"><i class="cb"></i>Asian &nbsp;&nbsp;&nbsp;<i class="cb"></i>Multicultural &nbsp;&nbsp;&nbsp;<i class="cb"></i>Native Hawaiian or Other Pacific Islander</div>
  <div class="t sm" style="left:711px;top:559px"><i class="cb"></i>Other Race &nbsp;&nbsp;<i class="cb"></i>White &nbsp;&nbsp;<i class="cb"></i>Does not wish to disclose &nbsp;&nbsp;<i class="cb"></i>Not provided</div>
  <div class="vl" style="left:1227px;top:507px;height:73px"></div>
  <div class="t sm" style="left:1237px;top:514px"><b>Ethnicity:</b> <i class="cb"></i>Hispanic or Latino</div>
  <div class="t sm" style="left:1237px;top:535px"><i class="cb"></i>Not Hispanic or Latino</div>
  <div class="t sm" style="left:1237px;top:559px"><i class="cb"></i>Unknown</div>
  <div class="hl" style="left:697px;top:580px;width:777px"></div>

  <div class="t sm" style="left:711px;top:591px"><b>Gender Identity:</b> <i class="cb"></i>Male &nbsp;&nbsp;<i class="cb"></i>Female &nbsp;&nbsp;<i class="cb"></i>Gender nonconforming &nbsp;&nbsp;<i class="cb"></i>Transgender male-to-female</div>
  <div class="t sm" style="left:711px;top:613px"><i class="cb"></i>Transgender female-to-male &nbsp;&nbsp;<i class="cb"></i>Does not wish to disclose &nbsp;&nbsp;<i class="cb"></i>Not provided &nbsp;&nbsp;<i class="cb"></i>Not applicable</div>
  <div class="hl" style="left:697px;top:633px;width:777px"></div>
  <div class="t sm" style="left:711px;top:642px"><b>Sexual Orientation:</b> <i class="cb"></i>Bisexual &nbsp;&nbsp;<i class="cb"></i>Straight &nbsp;&nbsp;<i class="cb"></i>Gay or Lesbian &nbsp;&nbsp;<i class="cb"></i>Something Else &nbsp;&nbsp;<i class="cb"></i>Not applicable</div>
  <div class="t sm" style="left:711px;top:663px"><i class="cb"></i>Not provided &nbsp;&nbsp;<i class="cb"></i>Does not wish to disclose</div>
  <div class="hl thick" style="left:697px;top:694px;width:777px"></div>

  <!-- Billing -->
  <div class="t" style="left:723px;top:702px;font-size:26px;font-weight:500">Billing Information <span style="font-size:20px;font-weight:700">(Please include a copy of the front &amp; back of card.)</span></div>
  <div class="hl" style="left:697px;top:733px;width:777px"></div>
  <div class="t lbl" style="left:709px;top:739px">Billing Type: &nbsp;<i class="cb"></i>Patient</div>
  <div class="t lbl" style="left:938px;top:739px"><i class="cb"></i>Insurance</div>
  <div class="t lbl" style="left:1094px;top:739px"><i class="cb"></i>Client</div>
  <div class="hl" style="left:697px;top:759px;width:777px;height:1px"></div>
  <div class="t lbl" style="left:709px;top:764px"><span class="req">Relation (Required):</span> &nbsp;<i class="cb"></i>Self</div>
  <div class="t lbl" style="left:941px;top:764px"><i class="cb"></i>Spouse</div>
  <div class="t lbl" style="left:1039px;top:764px"><i class="cb"></i>Depenant Insured’s Name (if not patient):</div>
  <div class="hl" style="left:697px;top:798px;width:777px"></div>
  <div class="t lbl" style="left:709px;top:803px">Insured’s SS#:</div>
  <div class="vl" style="left:1100px;top:798px;height:40px"></div>
  <div class="t lbl" style="left:1107px;top:803px">Insured’s DOB:</div>
  <div class="hl" style="left:697px;top:838px;width:777px"></div>
  <div class="t lbl" style="left:709px;top:843px">Primary Insurance Carrier:</div>
  <div class="vl" style="left:1048px;top:838px;height:42px"></div>
  <div class="t lbl" style="left:1055px;top:843px">Medicare, Medicaid or Policy ID#:</div>
  <div class="hl" style="left:697px;top:879px;width:777px"></div>
  <div class="t lbl" style="left:709px;top:884px">Claim Address:</div>
  <div class="hl" style="left:697px;top:919px;width:777px"></div>
  <div class="t lbl" style="left:709px;top:924px">Employer/Group Name:</div>
  <div class="vl" style="left:1048px;top:919px;height:54px"></div>
  <div class="t lbl" style="left:1055px;top:924px">Group#:</div>
  <div class="hl thick" style="left:697px;top:972px;width:777px"></div>

  <!-- Wound / sepsis -->
  <div class="t" style="left:711px;top:992px;font-size:28px;font-weight:500">Location of Infection:</div>
  <div class="hl" style="left:1000px;top:1017px;width:462px;height:4px"></div>
  <div class="pcr-band"></div>
  <div class="pcr-box"></div>
  <div class="t pcr-title" style="left:907px;top:1039px">Wound/Sepsis PCR Panel</div>
  <div class="t" style="left:1329px;top:1050px;font-size:19px;font-weight:500">Panel includes</div>

  <div class="t group-head" style="left:697px;width:777px;text-align:center;top:1083px">BACTERIA</div>
  <div class="t org" style="left:727px;top:1114px;line-height:35px">Escherichia coli<br>Streptococcus agalactiae<br>Klebsiella oxytoca<br>Staphylococcus saprophyticus<br>Pseudomonas aeruginosa<br>Staphylococcus haemolyticus<br>Enterococcus faecium<br>Enterococcus faecalis<br>Acinetobacter calcoaceticus-baumannii complex</div>
  <div class="t org" style="left:1140px;top:1114px;line-height:35px">Klebsiella aerogenes<br>Klebsiella pneumoniae<br>Staphylococcus aureus<br>Streptococcus pyogenes<br>Streptococcus pneumoniae<br>Streptococcus dysgalactiae<br>Staphylococcus lugdunensis<br>Staphylococcus epidermidis</div>

  <div class="t group-head" style="left:697px;width:777px;text-align:center;top:1438px">FUNGI</div>
  <div class="t org" style="left:727px;top:1468px;line-height:32.5px">Candida krusei<br>Candida tropicalis<br>Candida glabrata</div>
  <div class="t org" style="left:977px;top:1468px;line-height:32.5px">Candida albicans<br>Fusarium solani<br>Microsporum spp</div>
  <div class="t org" style="left:1227px;top:1468px;line-height:32.5px">Candida parapsilosis<br>Trichophyton spp</div>

  <div class="t" style="left:697px;width:800px;text-align:center;top:1581px;font-size:27px;font-weight:700">ANTIMICROBIAL RESISTANCE</div>
  <div class="t org" style="left:697px;width:800px;text-align:center;top:1611px">Methicillin Resistance (MecA+C)</div>

  <div class="hl" style="left:22px;top:1671px;width:1453px"></div>

  <!-- Other test -->
  <div class="t" style="left:35px;top:1688px;font-size:32px;font-weight:700">Other Test/Panel</div>
  <div class="t" style="left:727px;top:1688px;font-size:24px;font-weight:500;line-height:1.1">ICD10 codes<br><span class="req" style="font-weight:400">(required):</span></div>

  <!-- Clinical notes -->
  <div class="hl" style="left:22px;top:1860px;width:1453px"></div>
  <div class="t clin-label" style="left:35px;top:1880px">Clinical Impression:</div>
  <div class="write-line" style="left:245px;top:1900px;width:1215px"></div>
  <div class="write-line" style="left:35px;top:1928px;width:1425px"></div>
  <div class="t clin-label" style="left:35px;top:1946px">Clinical History:</div>
  <div class="write-line" style="left:210px;top:1966px;width:1250px"></div>
  <div class="write-line" style="left:35px;top:1992px;width:1425px"></div>

  <!-- Authorization -->
  <div class="t" style="left:22px;top:2016px;font-size:19px;font-weight:700">Physician Authorization</div>
  <div class="fine" style="top:2040px">I, the undersigned healthcare provider, acknowlegde that when ordering a Urinary Tract Infection (UTI), Nail, or Wound PCR panel through Crestline Labs, located at 4120 Harborview Pkwy, Suite 210, Lakeview, MI 48900 (NPI: 1000000000, Tax ID: 000000000) I understand and agree to the following terms:<br>
  1. In some or all instances, UTI, Wound, and Nail panels and their associated antibiotic resistance markers tests will be forwarded to Meridian PCR Group (880 Cedar Ridge Dr, Ste 140, Oakfield, TX 78600; Phone: (555) 456-0190; Fax: (555) 456-0191 for processing and analysis.<br>
  2. Any pathology, cytology, and thin prep specimens will be forwarded to Northgate Pathology Laboratory (2250 Elmwood Ave, Ste 102, Brookline Heights, MI 48900; Phone (555) 262-0188; podiatric Pathology Form Fax: (555) 262-0189) for evaluation and reporting.<br>
  3. I understand that while the initial order is placed with Crestline Labs, the actual testing may be performed by their partner laboratories as specified above.<br>
  4. I acknowledge that this referral process may affect billing procedures and timeline for results, and I accept this as part of the standard operating procedure for these specific test types.<br>
  5. I confirm that I have informed my patients about this testing arrangement as appropriate and in accordance with applicable regulations.</div>

  <div class="t" style="left:812px;top:2217px;font-size:16px;font-weight:700">Physician Signature</div>
  <div class="sig-line" style="left:975px;top:2230px;width:293px"></div>
  <div class="t" style="left:1280px;top:2217px;font-size:16px;font-weight:700">Date:</div>
  <div class="sig-line" style="left:1328px;top:2230px;width:138px"></div>

  <div class="t" style="left:22px;top:2229px;font-size:19px;font-weight:700">Patient Consent and Authorization</div>
  <div class="fine" style="top:2256px">I authorize the release of my medical iformation including test results for submission of personalized reports to my healthcare providers and insurance carrier(s). I request that payment of benefits be made to Crestline Labs, Inc. on my behalf. If my policy does not allow for direct payment, I agree to relinquish allocated funds to Crestline Labs, Inc as compensation for services rendered. I also acknowledge that I will be liable for payment of deductibles, co payments and/or co insurance as detailed by my healthcare insurer. I understand that I am liable for charges not covered by my healthcare insurer. I also authorize Crestline Labs, Inc to appeal insurance claims on my behalf. I acknowledge the benefits, risk and limitations of this testing as describe to me by a qualified healthcare provider. My insurance may not cover or pay full amount for testing; I may be responsible for full or part of amount charged due to out of network benefits, deductible and co pays. Crestline Labs, Inc has my permission to bill my insurance carrier(s), this notice gives me the option to proceed with the procedure or decline. By signing this I have read all of the above and understand it. Medicare Advance Beneficiary Notice: Medicare will only pay for services that it determines to be reasonably and necessary under section 1882 (a) (1) of the Medicare Law. If Medicare determines that a particular service, although it would otherwise be covered, is not reasonable and necessary under the Medicare Program standards, Medicare will deny payment for that service. Medicare usually does not pay for these test for the reported diagnosis. By signing the Patient/Responsible Party Signature on this requisition, you are confirming your agreement to assume financial responsibility for the payment of these tests.</div>

  <div class="t" style="left:812px;top:2425px;font-size:16px;font-weight:700">Physician Signature</div>
  <div class="sig-line" style="left:975px;top:2438px;width:293px"></div>
  <div class="t" style="left:1280px;top:2425px;font-size:16px;font-weight:700">Date:</div>
  <div class="sig-line" style="left:1328px;top:2438px;width:138px"></div>

</div>
</div>
</body>
</html>
```